Corvena Hotel, city center modern minimal hotel operating all year round, on Rhodes island Greece

city, modern ,all year operating hotel

Target Market(s)

tourists, business agents

Industry/Entity Type

tourism

Coding

Coded - Design and coding required

Number of Pages Required

2 page

Requirements
Must have
• room type photos and descriptions, amenities individual listing (graphic), comments sections, map driving location details
Nice to have
• gallery section, modern and minimal design, amenities section, individual room type descriptions, photos and facilities

```html
<!DOCTYPE html>
<html lang="en">
<head>
<meta charset="utf-8">
<title>Corvena Hotel Rhodes</title>
<link href="https://fonts.googleapis.com/css2?family=Playfair+Display:wght@400;700&family=Mulish:wght@400;600;700&display=swap" rel="stylesheet">
<style>
:root{
  --green:#1f5a3a;
  --green-dark:#15321f;
  --navy:#14294f;
  --gold:#c9a23f;
  --ink:#222;
  --muted:#666;
  --light:#eef2f5;
  --card:#f1f1f1;
  --line:#d9d9d9;
}
*{margin:0;padding:0;box-sizing:border-box}
html,body{width:1200px;height:3876px;overflow:hidden;background:#fff}
body{position:relative;font-family:'Mulish',sans-serif;color:var(--ink)}
.abs{position:absolute}
.serif{font-family:'Playfair Display',serif}

/* header */
.site-header{position:absolute;top:0;left:0;width:1200px;height:60px;background:#fff;border-bottom:1px solid #eee}
.brand{position:absolute;left:130px;top:12px;display:flex;align-items:center;gap:10px}
.brand-mark{width:26px;height:26px;background:var(--green)}
.brand-name{font-family:'Playfair Display',serif;font-size:26px;color:var(--green);letter-spacing:1px}
.main-nav{position:absolute;top:22px;left:604px;display:flex;gap:50px;font-family:'Playfair Display',serif;font-size:12px}
.btn-book{position:absolute;left:958px;top:15px;width:112px;height:32px;background:var(--gold);color:#fff;font-family:'Playfair Display',serif;font-size:12px;display:flex;align-items:center;justify-content:center}

/* hero */
.hero-photo{position:absolute;left:0;top:60px;width:925px;height:540px;background:linear-gradient(180deg,#55606a 0%,#2a3540 60%,#1e2a36 100%)}
.hero-kicker{left:130px;top:238px;color:#fff;font-family:'Playfair Display',serif;font-size:16px;letter-spacing:1px}
.hero-title{left:130px;top:260px;color:#fff;font-family:'Playfair Display',serif;font-weight:700;font-size:43px;line-height:48px}
.btn-explore{left:130px;top:383px;width:128px;height:35px;background:#fff;font-family:'Playfair Display',serif;font-size:12px;display:flex;align-items:center;padding-left:16px}
.diamond-dot{position:absolute;width:14px;height:14px;background:var(--gold);transform:rotate(45deg)}
.hero-art{left:676px;top:150px;width:510px;height:300px}

/* booking */
.booking{left:130px;top:543px;width:940px;height:114px;background:var(--navy)}
.booking-label{position:absolute;top:24px;width:100%;text-align:center;color:#cfd6e3;font-size:10px;letter-spacing:2px}
.field{position:absolute;top:51px;height:37px;background:#fff;font-size:8px;letter-spacing:1px;color:#666;display:flex;align-items:center;padding-left:12px}
.btn-search{position:absolute;top:51px;left:698px;width:173px;height:37px;background:#1d7a3e;color:#fff;font-size:11px;font-weight:700;letter-spacing:2px;display:flex;align-items:center;justify-content:center}

/* about */
.about-art{left:130px;top:725px;width:392px;height:275px}
.kicker{font-family:'Playfair Display',serif;font-size:11px;letter-spacing:.5px}
.section-title{font-family:'Playfair Display',serif;font-size:36px;line-height:44px}
.about-text{left:612px;top:822px;width:460px;font-size:12px;line-height:20px;color:#555}
.about-text p{margin-bottom:12px}
.btn-green{background:var(--green);color:#fff;font-family:'Playfair Display',serif;font-size:12px;display:flex;align-items:center;justify-content:center}
.watermark{left:230px;top:1015px;font-family:'Playfair Display',serif;font-size:140px;color:#f1f1f1;letter-spacing:4px}
.rule{position:absolute;left:0;width:160px;height:1px;background:#ccc}
.rule::after{content:"";position:absolute;left:130px;top:-1px;width:30px;height:3px;background:var(--gold)}

/* rooms */
.room{position:absolute;width:300px;height:370px}
.room-head{position:absolute;left:0;top:0;width:300px;height:216px;background:var(--card)}
.room-title{position:absolute;top:12px;width:100%;text-align:center;font-family:'Playfair Display',serif;font-weight:700;font-size:16px}
.room-photo{position:absolute;left:13px;top:41px;width:274px;height:174px}
.room-desc{position:absolute;left:0;top:230px;width:290px;font-size:11px;line-height:17px;color:#666}
.room-icons{position:absolute;left:0;top:283px;width:290px;display:flex;align-items:center;gap:12px;padding-left:5px}
.ico{width:28px;height:28px;border:1px solid #ccc;border-radius:50%;display:flex;align-items:center;justify-content:center}
.comments{margin-left:auto;font-size:9px;color:#888}
.comments b{color:#222}
.room-price{position:absolute;left:0;top:330px;width:115px;height:35px}
.room-view{position:absolute;left:118px;top:330px;width:112px;height:35px;border:1px solid #999;font-family:'Playfair Display',serif;font-size:12px;display:flex;align-items:center;justify-content:center}

/* features */
.features{left:0;top:2090px;width:1200px;height:328px;background:var(--light)}
.feature{position:absolute;width:240px;text-align:center}
.feature + .feature{border-left:1px solid #dde2e6}
.feat-icon{position:absolute;left:50%;margin-left:-44px;width:88px;height:88px}
.feat-title{font-family:'Playfair Display',serif;font-size:20px}
.feat-text{font-size:11px;line-height:19px;color:#555;margin:10px auto 0;width:200px}

/* gallery */
.gallery-side{top:2620px;height:325px}
.gallery-main{left:350px;top:2624px;width:502px;height:328px;background:#fff;box-shadow:0 2px 10px rgba(0,0,0,.25);padding:6px}
.arrow{width:32px;height:32px;background:#fff;border-radius:50%;display:flex;align-items:center;justify-content:center;box-shadow:0 1px 4px rgba(0,0,0,.2)}

/* testimonials */
.testimonials{left:0;top:3025px;width:1200px;height:473px;background:var(--light)}
.quote{position:absolute;top:3170px;width:300px;height:146px;background:#fff;padding:34px 22px;text-align:center;font-size:11px;line-height:17px;color:#444}
.avatar{position:absolute;top:3327px;width:56px;height:56px;border-radius:50%}
.client{position:absolute;top:3418px;width:300px;text-align:center}
.client-name{font-family:'Playfair Display',serif;font-size:12px;letter-spacing:1.5px}
.client-place{font-size:9px;color:#777;margin-top:4px}

/* footer */
.footer{left:0;top:3498px;width:1200px;height:378px;background:linear-gradient(180deg,#1d3a27 0%,#13271a 100%);color:#fff}
.foot-head{font-family:'Playfair Display',serif;font-size:17px;color:var(--gold)}
.foot-links{font-size:11px;line-height:27px}
.contact-row{display:flex;align-items:center;gap:8px;font-size:11px;line-height:14px}
.contact-ico{width:28px;height:28px;border:1px solid #fff;border-radius:50%;display:flex;align-items:center;justify-content:center;flex-shrink:0}
.social{width:28px;height:28px;border-radius:50%;background:var(--gold)}
.vsep{position:absolute;top:3530px;width:1px;height:240px;background:rgba(255,255,255,.12)}
.copyright{position:absolute;top:3838px;width:1200px;text-align:center;font-size:8px;letter-spacing:.5px}
.copyright span{color:var(--gold)}
</style>
</head>
<body>

<header class="site-header">
  <div class="brand"><span class="brand-mark"></span><span class="brand-name">Corvena</span></div>
  <nav class="main-nav"><span>Home</span><span>Room</span><span>Gallery</span><span>Contact Us</span></nav>
  <div class="btn-book">Book Now</div>
</header>

<div class="hero-photo" role="img" aria-label="Hotel building and pool terrace at dusk"></div>
<div class="abs hero-kicker">FEW STEPS TO</div>
<div class="abs hero-title">Interesting Places<br>In The Perfect Location</div>
<div class="abs btn-explore">EXPLORE MORE<span class="diamond-dot" style="right:-7px;top:11px"></span></div>
<svg class="abs hero-art" viewBox="0 0 510 300" role="img" aria-label="Diamond collage of hotel views in green and gold">
  <polygon points="80,150 180,50 280,150 180,250" fill="#d9b545" opacity=".85"/>
  <polygon points="340,150 420,70 510,150 420,230" fill="#e0bf55" opacity=".85"/>
  <polygon points="130,150 260,5 400,150 260,295" fill="#1a8a4a"/>
  <polygon points="150,150 260,40 370,150 260,260" fill="#0f5e32"/>
</svg>

<section class="abs booking">
  <div class="booking-label">BOOK NOW YOUR HOTEL</div>
  <div class="field" style="left:68px;width:174px">CHECK IN</div>
  <div class="field" style="left:248px;width:174px">CHECK OUT</div>
  <div class="field" style="left:430px;width:126px">ADULTS</div>
  <div class="field" style="left:564px;width:126px">CHILDREEN</div>
  <div class="btn-search">SEARCH</div>
</section>

<svg class="abs about-art" viewBox="0 0 392 275" role="img" aria-label="Diamond collage of Rhodes sea views and white chapels">
  <polygon points="5,135 135,12 265,135 135,258" fill="#2f7fb8"/>
  <polygon points="195,75 265,5 332,75 265,145" fill="#3a8cc6"/>
  <polygon points="195,140 262,75 390,140 262,255" fill="#d8c9a8"/>
  <polygon points="0,245 45,200 95,245 45,290" fill="#c98a55"/>
</svg>
<div class="abs kicker" style="left:612px;top:723px">ABOUT OUR</div>
<div class="abs section-title" style="left:612px;top:736px">Corvena Hotel Rhodes</div>
<div class="abs" style="left:612px;top:782px;width:160px;height:1px;background:#ccc"></div>
<div class="abs about-text">
  <p>Sed ut perspiciatis unde omnis iste natus error sit voluptatem accusantium doloremque laudantium, totam rem aperiam, eaque ipsa quae ab illo inventore veritatis et quasi architecto beatae vitae dicta sunt explicabo. Nemo enim ipsam voluptatem quia voluptas sit aspernatur aut odit aut fugit, sed quia consequuntur magni dolores eos qui ratione voluptatem sequi nesciunt.</p>
  <p>Sed ut perspiciatis unde omnis iste natus error sit voluptatem accusantium doloremque laudantium, totam rem aperiam...</p>
</div>
<div class="abs watermark">WELCOME</div>
<div class="abs btn-green" style="left:612px;top:1004px;width:128px;height:35px">READ MORE<span class="diamond-dot" style="right:-7px;top:11px"></span></div>

<div class="abs kicker" style="left:130px;top:1119px">CORVENA HOTEL</div>
<div class="abs section-title" style="left:130px;top:1133px">Our Rooms</div>
<div class="rule" style="top:1186px"></div>

<!-- room cards -->
<article class="room" style="left:130px;top:1213px">
  <div class="room-head"><div class="room-title">Apartment For 4 Adults</div><div class="room-photo" role="img" aria-label="Apartment bedroom with city view" style="background:linear-gradient(135deg,#8a8884,#3f3b36)"></div></div>
  <p class="room-desc">Situated on the top floor of the hotel, this fully air-conditioned apartment...</p>
  <div class="room-icons"><span class="ico"><svg width="14" height="10"><path d="M1 9V3h12v6M1 6h12" stroke="#666" fill="none"/></svg></span><span class="ico"><svg width="14" height="12"><path d="M1 6h12v2a3 3 0 01-3 3H4a3 3 0 01-3-3z" stroke="#666" fill="none"/></svg></span><span class="ico"><svg width="12" height="12"><rect x="1" y="1" width="10" height="10" stroke="#666" fill="none"/></svg></span><span class="comments">Comments: <b>52</b></span></div>
  <div class="room-price btn-green">Price: € 4.292</div><div class="room-view">View Location</div>
</article>
<article class="room" style="left:450px;top:1213px">
  <div class="room-head"><div class="room-title">Superior Double Room</div><div class="room-photo" role="img" aria-label="Superior double room interior" style="background:linear-gradient(135deg,#9c8a72,#4a3e30)"></div></div>
  <p class="room-desc">Situated on the top floor of the hotel, this fully air-conditioned apartment...</p>
  <div class="room-icons"><span class="ico"><svg width="14" height="10"><path d="M1 9V3h12v6M1 6h12" stroke="#666" fill="none"/></svg></span><span class="ico"><svg width="14" height="12"><path d="M1 6h12v2a3 3 0 01-3 3H4a3 3 0 01-3-3z" stroke="#666" fill="none"/></svg></span><span class="ico"><svg width="12" height="12"><rect x="1" y="1" width="10" height="10" stroke="#666" fill="none"/></svg></span><span class="comments">Comments: <b>52</b></span></div>
  <div class="room-price btn-green">Price: € 4.292</div><div class="room-view">View Location</div>
</article>
<article class="room" style="left:770px;top:1213px">
  <div class="room-head"><div class="room-title">Quadruple Room</div><div class="room-photo" role="img" aria-label="Quadruple room with white bed" style="background:linear-gradient(180deg,#7a7773,#c9c5bf)"></div></div>
  <p class="room-desc">Situated on the top floor of the hotel, this fully air-conditioned apartment...</p>
  <div class="room-icons"><span class="ico"><svg width="14" height="10"><path d="M1 9V3h12v6M1 6h12" stroke="#666" fill="none"/></svg></span><span class="ico"><svg width="14" height="12"><path d="M1 6h12v2a3 3 0 01-3 3H4a3 3 0 01-3-3z" stroke="#666" fill="none"/></svg></span><span class="ico"><svg width="12" height="12"><rect x="1" y="1" width="10" height="10" stroke="#666" fill="none"/></svg></span><span class="comments">Comments: <b>52</b></span></div>
  <div class="room-price btn-green">Price: € 4.292</div><div class="room-view">View Location</div>
</article>
<article class="room" style="left:130px;top:1608px">
  <div class="room-head"><div class="room-title">Triple Room</div><div class="room-photo" role="img" aria-label="Triple room with patterned rug" style="background:linear-gradient(135deg,#8c7a62,#d4ccc0)"></div></div>
  <p class="room-desc">Situated on the top floor of the hotel, this fully air-conditioned apartment...</p>
  <div class="room-icons"><span class="ico"><svg width="14" height="10"><path d="M1 9V3h12v6M1 6h12" stroke="#666" fill="none"/></svg></span><span class="ico"><svg width="14" height="12"><path d="M1 6h12v2a3 3 0 01-3 3H4a3 3 0 01-3-3z" stroke="#666" fill="none"/></svg></span><span class="ico"><svg width="12" height="12"><rect x="1" y="1" width="10" height="10" stroke="#666" fill="none"/></svg></span><span class="comments">Comments: <b>52</b></span></div>
  <div class="room-price btn-green">Price: € 4.292</div><div class="room-view">View Location</div>
</article>
<article class="room" style="left:450px;top:1608px">
  <div class="room-head"><div class="room-title">Single Room</div><div class="room-photo" role="img" aria-label="Single room lounge area" style="background:linear-gradient(135deg,#b7aa98,#6e604f)"></div></div>
  <p class="room-desc">Situated on the top floor of the hotel, this fully air-conditioned apartment...</p>
  <div class="room-icons"><span class="ico"><svg width="14" height="10"><path d="M1 9V3h12v6M1 6h12" stroke="#666" fill="none"/></svg></span><span class="ico"><svg width="14" height="12"><path d="M1 6h12v2a3 3 0 01-3 3H4a3 3 0 01-3-3z" stroke="#666" fill="none"/></svg></span><span class="ico"><svg width="12" height="12"><rect x="1" y="1" width="10" height="10" stroke="#666" fill="none"/></svg></span><span class="comments">Comments: <b>52</b></span></div>
  <div class="room-price btn-green">Price: € 4.292</div><div class="room-view">View Location</div>
</article>
<article class="room" style="left:770px;top:1608px">
  <div class="room-head"><div class="room-title">Double Room</div><div class="room-photo" role="img" aria-label="Double room with warm lighting" style="background:linear-gradient(135deg,#8a6a4a,#c9b08a)"></div></div>
  <p class="room-desc">Situated on the top floor of the hotel, this fully air-conditioned apartment...</p>
  <div class="room-icons"><span class="ico"><svg width="14" height="10"><path d="M1 9V3h12v6M1 6h12" stroke="#666" fill="none"/></svg></span><span class="ico"><svg width="14" height="12"><path d="M1 6h12v2a3 3 0 01-3 3H4a3 3 0 01-3-3z" stroke="#666" fill="none"/></svg></span><span class="ico"><svg width="12" height="12"><rect x="1" y="1" width="10" height="10" stroke="#666" fill="none"/></svg></span><span class="comments">Comments: <b>52</b></span></div>
  <div class="room-price btn-green">Price: € 4.292</div><div class="room-view">View Location</div>
</article>

<!-- features -->
<section class="abs features">
  <div class="feature" style="left:120px;top:0;height:240px">
    <svg class="feat-icon" style="top:-46px" viewBox="0 0 88 88"><polygon points="44,2 86,44 44,86 2,44" fill="var(--green)"/><path d="M44 32a9 9 0 019 9c0 7-9 15-9 15s-9-8-9-15a9 9 0 019-9z" stroke="#fff" fill="none" stroke-width="1.5"/><circle cx="44" cy="41" r="3" stroke="#fff" fill="none" stroke-width="1.5"/></svg>
    <div style="margin-top:68px" class="feat-title">Location</div>
    <p class="feat-text">Medieval city is just a few steps away, so are the beautiful beaches of Elli and Psaropoula.</p>
    <span class="diamond-dot" style="left:113px;top:176px"></span>
  </div>
  <div class="feature" style="left:360px;top:30px;height:240px">
    <svg class="feat-icon" style="top:-48px" viewBox="0 0 88 88"><polygon points="44,2 86,44 44,86 2,44" fill="var(--green)"/><circle cx="44" cy="44" r="11" stroke="#fff" fill="none" stroke-width="1.5" stroke-dasharray="4 2"/><circle cx="44" cy="44" r="5" stroke="#fff" fill="none" stroke-width="1.5"/></svg>
    <div style="margin-top:66px" class="feat-title">Operation</div>
    <p class="feat-text">Famous for its friendliness, cleanliness and various amenities found only in higher...</p>
    <span class="diamond-dot" style="left:113px;top:174px"></span>
  </div>
  <div class="feature" style="left:600px;top:30px;height:260px">
    <svg class="feat-icon" style="top:-18px" viewBox="0 0 88 88"><polygon points="44,2 86,44 44,86 2,44" fill="var(--green)"/><path d="M44 52l-9-9a5 5 0 019-5 5 5 0 019 5z" stroke="#fff" fill="none" stroke-width="1.5"/></svg>
    <div style="margin-top:108px" class="feat-title">Friendliness</div>
    <p class="feat-text">The hotel offers its services to both local and international guests either family or business type.</p>
    <span class="diamond-dot" style="left:113px;top:216px"></span>
  </div>
  <div class="feature" style="left:840px;top:30px;height:260px">
    <svg class="feat-icon" style="top:10px" viewBox="0 0 88 88"><polygon points="44,2 86,44 44,86 2,44" fill="var(--green)"/><rect x="34" y="38" width="9" height="14" stroke="#fff" fill="none" stroke-width="1.5"/><rect x="46" y="36" width="9" height="16" stroke="#fff" fill="none" stroke-width="1.5"/></svg>
    <div style="margin-top:134px" class="feat-title">Amenities</div>
    <p class="feat-text">The hotel offers most modern amenities, like satellite television set, mini bar, en sure bathroom...</p>
    <span class="diamond-dot" style="left:113px;top:242px"></span>
  </div>
</section>

<!-- gallery -->
<div class="abs kicker" style="left:130px;top:2484px">GALLERY</div>
<div class="abs section-title" style="left:130px;top:2498px">Discover The Corvena</div>
<div class="rule" style="top:2552px"></div>
<div class="abs serif" style="left:130px;top:2566px;font-size:12px;color:#444">Sed ut perspiciatis unde omnis iste natus error sit voluptatem accusantium</div>
<div class="abs gallery-side" role="img" aria-label="Guests checking in at reception desk" style="left:0;width:350px;background:linear-gradient(90deg,#fff 0%,#d9d4cc 55%,#bdb6ac 100%)"></div>
<div class="abs gallery-side" role="img" aria-label="Guest relaxing on a sunlit deck" style="left:852px;width:348px;background:linear-gradient(90deg,#d8c7b4 0%,#ece7e2 60%,#fff 100%)"></div>
<div class="abs gallery-main"><div role="img" aria-label="Bright white suite living area" style="width:100%;height:100%;background:linear-gradient(180deg,#c8cdd2,#8f969d 60%,#b7bcc1)"></div></div>
<div class="abs arrow" style="left:324px;top:2774px"><svg width="8" height="10"><path d="M6 1L2 5l4 4" stroke="#222" fill="none" stroke-width="1.5"/></svg></div>
<div class="abs arrow" style="left:846px;top:2774px"><svg width="8" height="10"><path d="M2 1l4 4-4 4" stroke="#222" fill="none" stroke-width="1.5"/></svg></div>

<!-- testimonials -->
<section class="abs testimonials"></section>
<div class="abs kicker" style="left:130px;top:3066px">TESTIMONIALS</div>
<div class="abs section-title" style="left:130px;top:3080px">Our Client Says</div>
<div class="rule" style="top:3135px"></div>
<div class="quote" style="left:130px">Sed ut perspiciatis unde omnis iste natus error sit voluptatem accusantium doloremque laudantium, totam rem aperiam, eaque ipsa quae ab illo inventore veritatis et quasi architecto beatae</div>
<div class="quote" style="left:450px">Sed ut perspiciatis unde omnis iste natus error sit voluptatem accusantium doloremque laudantium, totam rem aperiam, eaque ipsa quae ab illo inventore veritatis et quasi architecto beatae</div>
<div class="quote" style="left:770px">Sed ut perspiciatis unde omnis iste natus error sit voluptatem accusantium doloremque laudantium, totam rem aperiam, eaque ipsa quae ab illo inventore veritatis et quasi architecto beatae</div>
<div class="avatar" role="img" aria-label="Guest portrait" style="left:252px;background:#8a7466"></div>
<div class="avatar" role="img" aria-label="Guest portrait" style="left:572px;background:#d9b79a"></div>
<div class="avatar" role="img" aria-label="Guest portrait" style="left:892px;background:#b8927a"></div>
<div class="client" style="left:130px"><div class="client-name">MARCO DELANE</div><div class="client-place">UK, Brighton</div></div>
<div class="client" style="left:450px"><div class="client-name">MARCO DELANE</div><div class="client-place">UK, Brighton</div></div>
<div class="client" style="left:770px"><div class="client-name">MARCO DELANE</div><div class="client-place">UK, Brighton</div></div>

<!-- footer -->
<footer class="abs footer"></footer>
<div class="abs" style="left:130px;top:3556px;display:flex;align-items:center;gap:12px"><span style="width:30px;height:30px;background:var(--gold)"></span><span class="serif" style="font-size:32px;color:#fff;letter-spacing:2px">Corvena</span></div>
<div class="abs" style="left:130px;top:3647px;display:flex;gap:13px"><span class="social"></span><span class="social"></span><span class="social"></span></div>
<div class="vsep" style="left:378px"></div>
<div class="vsep" style="left:825px"></div>
<div class="abs foot-head" style="left:430px;top:3530px">Quick Links</div>
<div class="abs foot-links" style="left:430px;top:3564px;color:#fff">Home<br>Rooms<br>Gallery<br>Contact Us</div>
<div class="abs foot-head" style="left:590px;top:3530px">Contact Us</div>
<div class="abs" style="left:590px;top:3566px;display:flex;flex-direction:column;gap:28px">
  <div class="contact-row"><span class="contact-ico"><svg width="10" height="13"><path d="M5 1a4 4 0 014 4c0 3-4 7-4 7S1 8 1 5a4 4 0 014-4z" stroke="#fff" fill="none"/></svg></span>14 Anemonis Street, Rhodes<br>851 00</div>
  <div class="contact-row"><span class="contact-ico"><svg width="12" height="12"><path d="M2 1l3 3-1.5 1.5a7 7 0 003 3L8 7l3 3-2 2C5 12 0 7 0 3z" stroke="#fff" fill="none"/></svg></span>+30 2241 000 555</div>
  <div class="contact-row"><span class="contact-ico"><svg width="12" height="9"><rect x=".5" y=".5" width="11" height="8" stroke="#fff" fill="none"/><path d="M.5.5L6 5l5.5-4.5" stroke="#fff" fill="none"/></svg></span>info@corvenahotel.example</div>
</div>
<div class="abs foot-head" style="left:850px;top:3530px">Newsletter</div>
<div class="abs" style="left:850px;top:3570px;width:220px;height:32px;background:#fff;color:#333;font-size:9px;display:flex;align-items:center;padding-left:10px">Enter Your Email</div>
<div class="abs" style="left:850px;top:3606px;width:220px;height:32px;background:var(--gold);color:#fff;font-size:10px;font-weight:700;display:flex;align-items:center;justify-content:center">SUBSCRIBE</div>
<div class="abs" style="left:578px;top:3776px;width:44px;height:30px;border-radius:4px;background:rgba(255,255,255,.85)"></div>
<div class="copyright" style="color:#fff">COPYRIGHT © 2022 <span>CORVENA CITY HOTEL RHODES</span>. ALL RIGHTS RESERVED.</div>

</body>
</html>
```